Real State Agency App

We need an app design for a real state agency, we provide mockups for our project that ilustrates very well what we need
our web site is www.brightkeyhomes-example.com,

Target Market(s)

Tourism

Font styles to use
Other font styles liked:
• attached you will find it

Requirements
Must have
• Colors like the logo

```html
<!DOCTYPE html>
<html lang="en">
<head>
<meta charset="utf-8">
<title>Bright Key Homes – App Screens</title>
<link href="https://fonts.googleapis.com/css2?family=Catamaran:wght@400;500;600&display=swap" rel="stylesheet">
<style>
:root{
  --page:#ffffff;
  --screen:#e0e0e0;
  --band:#ffffff;
  --navy:#10243a;
  --ink:#1d1d1d;
  --muted:#8a8a8a;
  --line:#9aa0a6;
  --icon-stroke:#a9a9a9;
  --brand:#1f3f8f;
  --link:#2a6fd6;
  --accent:#d42020;
}
*{box-sizing:border-box;margin:0;padding:0}
html,body{width:1200px;height:1200px;overflow:hidden;background:var(--page)}
body{position:relative;font-family:"Catamaran",sans-serif;color:var(--ink)}
.screen{position:absolute;width:220px;height:480px;background:var(--screen);border-radius:26px;overflow:hidden;box-shadow:0 0 0 1px #d2d2d2}
.abs{position:absolute}
.nav-home{position:absolute;left:20px;top:30px;width:20px;height:20px}
.nav-right{position:absolute;right:20px;top:30px;width:18px;height:18px}
.hero-icon{position:absolute;left:50%;transform:translateX(-50%);top:72px;width:44px;height:50px}
.screen-title{position:absolute;left:0;right:0;top:130px;text-align:center;font-size:13px;font-weight:500}
.body-copy{position:absolute;left:36px;right:36px;font-size:7.6px;line-height:9.6px;text-align:justify;text-align-last:left}
.form{position:absolute;left:0;right:0;background:var(--band);padding-left:16px}
.field{height:19px;border-bottom:1px solid var(--line);font-size:6.4px;color:var(--muted);padding-top:6px;position:relative}
.field .chev{position:absolute;right:18px;top:6px;font-size:6px}
.field.tall{height:36px;border-bottom:none}
.field.tall .up{position:absolute;right:18px;bottom:3px;font-size:6px}
.btn{position:absolute;left:50%;transform:translateX(-50%);background:var(--navy);color:#fff;font-size:8px;padding:6px 4px 4px;white-space:nowrap;border-radius:1px}
/* menu */
.logo{position:absolute;left:0;right:0;top:50px;text-align:center;font-size:22px;font-weight:600;color:var(--brand)}
.logo .dot{display:inline-block;width:8px;height:8px;border-radius:50%;background:var(--brand);margin-left:4px;vertical-align:middle}
.menu-item{position:absolute;left:0;right:0;height:44px;background:var(--band);display:flex;align-items:center;font-size:10px;font-weight:500;border-bottom:2px solid #cfcfcf}
.menu-item svg{width:24px;height:24px;margin:0 14px 0 12px}
.langs{position:absolute;left:0;right:0;top:448px;text-align:center;font-size:8px}
.langs u{text-decoration:underline}
/* search rows */
.srow{height:20.5px;border-bottom:1px solid var(--line);font-size:6.6px;padding:6px 0 0 16px;position:relative;background:var(--band)}
.srow.ph{color:var(--muted)}
.srow .chev{position:absolute;right:18px;top:4px;width:9px;height:9px}
/* services */
.svc{position:absolute;left:0;right:0;height:24px;background:var(--band);text-align:center;font-size:8px;padding-top:7px;border-bottom:2px solid #cfcfcf}
/* results */
.result{position:absolute;left:0;right:0;height:82px;background:var(--band);border-bottom:2px solid #cfcfcf}
.result .photo{position:absolute;top:4px;width:120px;height:74px}
.result .snip{position:absolute;top:28px;width:62px;font-size:4.6px;line-height:6px}
.snip b{font-weight:600}.snip .red{color:var(--accent)}.snip .lnk{color:var(--link);text-decoration:underline}
.pager{position:absolute;top:448px;font-size:6.5px;color:var(--muted)}
/* detail */
.detail-photo{position:absolute;left:0;right:0;top:58px;height:148px;background:linear-gradient(180deg,#6d7f94 0%,#c9a57a 45%,#4b4a44 70%,#1f3a55 100%)}
.detail-title{position:absolute;left:0;right:0;top:212px;text-align:center;font-size:13px;font-weight:500}
.request{position:absolute;left:0;right:0;top:396px;height:24px;background:var(--band);text-align:center;font-size:8px;padding-top:7px}
</style>
</head>
<body>

<svg width="0" height="0" style="position:absolute">
  <defs>
    <symbol id="ico-home" viewBox="0 0 24 24"><path d="M12 2 1 12h3v10h6v-6h4v6h6V12h3z" fill="#10243a"/><rect x="16" y="3" width="3" height="5" fill="#10243a"/></symbol>
    <symbol id="ico-search" viewBox="0 0 24 24"><circle cx="10" cy="10" r="7" fill="none" stroke="#10243a" stroke-width="1.6"/><path d="m15 15 7 7" stroke="#10243a" stroke-width="1.8" stroke-linecap="round"/></symbol>
    <symbol id="ico-menu" viewBox="0 0 24 24"><g fill="#10243a"><rect x="2" y="4" width="3" height="3"/><rect x="7" y="4.5" width="15" height="2"/><rect x="2" y="10.5" width="3" height="3"/><rect x="7" y="11" width="15" height="2"/><rect x="2" y="17" width="3" height="3"/><rect x="7" y="17.5" width="15" height="2"/></g></symbol>
    <symbol id="big-house" viewBox="0 0 44 50"><path d="M22 6 3 26h6v18h10V32h6v12h10V26h6z" fill="#fff" stroke="#a9a9a9" stroke-width="1.4" stroke-linejoin="round"/></symbol>
    <symbol id="big-search" viewBox="0 0 44 50"><circle cx="19" cy="21" r="14" fill="#fff" stroke="#a9a9a9" stroke-width="1.6"/><circle cx="19" cy="21" r="9" fill="none" stroke="#a9a9a9" stroke-width="1.2"/><path d="m29 31 10 11" stroke="#a9a9a9" stroke-width="5" stroke-linecap="round"/><path d="m29 31 10 11" stroke="#fff" stroke-width="3" stroke-linecap="round"/></symbol>
    <symbol id="big-phone" viewBox="0 0 44 50"><path d="M12 6c3-2 6-1 7 2l2 6c1 2 0 4-2 5l-2 1c1 5 5 11 10 14l2-1c2-1 4-1 5 1l4 5c1 2 0 4-2 5-4 3-9 3-14-2C14 33 9 24 8 16c-1-4 1-8 4-10z" fill="#fff" stroke="#a9a9a9" stroke-width="1.4"/></symbol>
    <symbol id="big-info" viewBox="0 0 44 60"><circle cx="22" cy="8" r="6" fill="#fff" stroke="#a9a9a9" stroke-width="1.4"/><path d="M16 20h10v30h4v6H14v-6h4V26h-2z" fill="#fff" stroke="#a9a9a9" stroke-width="1.4" stroke-linejoin="round"/></symbol>
    <symbol id="line-search" viewBox="0 0 24 24"><circle cx="10" cy="10" r="7.5" fill="none" stroke="#a9a9a9" stroke-width="1.2"/><circle cx="10" cy="10" r="5" fill="none" stroke="#a9a9a9" stroke-width="1"/><path d="m15.5 15.5 6 6" stroke="#a9a9a9" stroke-width="2.4" stroke-linecap="round"/></symbol>
    <symbol id="line-info" viewBox="0 0 24 24"><circle cx="12" cy="3.5" r="2.3" fill="none" stroke="#a9a9a9" stroke-width="1"/><path d="M10 8h3v12h2v2H9v-2h1V10H9z" fill="none" stroke="#a9a9a9" stroke-width="1"/></symbol>
    <symbol id="line-house" viewBox="0 0 24 24"><path d="M12 3 2 12h3v9h5v-6h4v6h5v-9h3z" fill="none" stroke="#a9a9a9" stroke-width="1.1" stroke-linejoin="round"/></symbol>
    <symbol id="line-phone" viewBox="0 0 24 24"><path d="M6 3c2-1 3 0 4 2l1 3c0 1 0 2-1 2.5l-1 .5c1 3 3 6 6 8l1-.5c1-.5 2 0 3 .5l2 3c.5 1 0 2-1 2.5-2 1.5-5 1-8-2C8 17 5 12 4.5 8 4 6 5 4 6 3z" fill="none" stroke="#a9a9a9" stroke-width="1"/></symbol>
    <symbol id="chev" viewBox="0 0 10 10"><path d="m1 3 4 4 4-4" fill="none" stroke="#333" stroke-width=".9"/></symbol>
  </defs>
</svg>

<!-- Home menu -->
<section class="screen" style="left:60px;top:70px">
  <div class="logo">Bright Key<span class="dot"></span></div>
  <div class="menu-item" style="top:122px"><svg><use href="#line-search"/></svg>Serach Our Properties</div>
  <div class="menu-item" style="top:184px"><svg><use href="#line-info"/></svg>Our Services</div>
  <div class="menu-item" style="top:246px"><svg><use href="#line-house"/></svg>Sell your Property with us</div>
  <div class="menu-item" style="top:308px"><svg><use href="#line-phone"/></svg>Contact</div>
  <div class="langs">Spain &nbsp;| &nbsp;<u>English</u> &nbsp;| &nbsp;German</div>
</section>

<!-- Sell property -->
<section class="screen" style="left:357px;top:70px">
  <svg class="nav-home"><use href="#ico-home"/></svg>
  <svg class="nav-right"><use href="#ico-search"/></svg>
  <svg class="hero-icon"><use href="#big-house"/></svg>
  <h2 class="screen-title">Sell Property with us</h2>
  <p class="body-copy" style="top:172px">Cuando usted esta considerando la posibilidad de vender su propiedad, siempre puede trater de venderla usted mismo o puede hacerlo a traves de una inmobiliaria profesional, cosmo somos Bright Key.</p>
  <div class="form" style="top:250px">
    <div class="field">Name</div>
    <div class="field">Surname</div>
    <div class="field">Phone</div>
    <div class="field">Email</div>
    <div class="field">Property Name</div>
    <div class="field tall">Property Description<span class="chev">&#8964;</span><span class="up">&#8963;</span></div>
  </div>
  <div class="btn" style="top:408px">Send us your property</div>
</section>

<!-- Search -->
<section class="screen" style="left:654px;top:70px">
  <svg class="nav-home"><use href="#ico-home"/></svg>
  <svg class="hero-icon"><use href="#big-search"/></svg>
  <h2 class="screen-title">Search Properties</h2>
  <div class="abs" style="left:0;right:0;top:166px;border-top:1px solid var(--line)">
    <div class="srow">To Reform<svg class="chev"><use href="#chev"/></svg></div>
    <div class="srow ph">Key</div>
    <div class="srow">Type<svg class="chev"><use href="#chev"/></svg></div>
    <div class="srow">Area<svg class="chev"><use href="#chev"/></svg></div>
  </div>
  <div class="btn" style="top:268px">Search Properties</div>
</section>

<!-- Contact -->
<section class="screen" style="left:951px;top:360px">
  <svg class="nav-home"><use href="#ico-home"/></svg>
  <svg class="nav-right"><use href="#ico-search"/></svg>
  <svg class="hero-icon"><use href="#big-phone"/></svg>
  <h2 class="screen-title">Contact us</h2>
  <div class="form" style="top:172px">
    <div class="field">Name</div>
    <div class="field">Surname</div>
    <div class="field">Phone</div>
    <div class="field">Email</div>
    <div class="field" style="color:var(--navy)">Property Name<span class="chev">&#8964;</span></div>
    <div class="field tall">Notes<span class="chev">&#8964;</span><span class="up">&#8963;</span></div>
  </div>
  <div class="btn" style="top:333px;font-size:6.8px;padding:7px 5px 5px">Send us your message</div>
</section>

<!-- Services -->
<section class="screen" style="left:60px;top:630px">
  <svg class="nav-home"><use href="#ico-home"/></svg>
  <svg class="nav-right"><use href="#ico-search"/></svg>
  <svg class="hero-icon" style="top:68px;height:56px"><use href="#big-info"/></svg>
  <h2 class="screen-title">Our Services</h2>
  <p class="body-copy" style="top:172px;left:36px;right:36px">Cala d' Or es un sitio emblematico de la costa del levante mallorquin. Esta zona costera y sus alrededores son uno de los primeros lugares turisticos de Mallorca y se encuentran a tan solo 45 minutos del aeropuerto y de la fabulosa capital de Palma.</p>
  <div class="svc" style="top:268px">SEGUROS</div>
  <div class="svc" style="top:302px">COMPRA</div>
  <div class="svc" style="top:335px">MANTENIMIENTOS</div>
  <div class="svc" style="top:370px">OBRAS Y REFORMAS</div>
</section>

<!-- Results -->
<section class="screen" style="left:357px;top:630px">
  <svg class="nav-home"><use href="#ico-home"/></svg>
  <svg class="nav-right"><use href="#ico-search"/></svg>
  <div class="abs" style="left:0;right:0;top:56px;text-align:center;font-size:10px">Search results for</div>
  <div class="abs" style="left:0;right:0;top:76px;text-align:center;font-size:8px"><span style="color:var(--muted)">Key:</span> Beach, &nbsp;<span style="color:var(--muted)">Type:</span> House, &nbsp;<span style="color:var(--muted)">Area:</span> Palma</div>
  <div class="abs" style="left:0;right:0;top:98px;height:2px;background:#cfcfcf"></div>
  <div class="result" style="top:100px">
    <div class="photo" role="img" aria-label="Photo of a white modern villa with pool and palm trees" style="left:0;background:linear-gradient(180deg,#9ec3e0,#e8ecef 50%,#39b4d6)"></div>
    <p class="snip" style="left:140px"><b>A paragraph of <span class="red">text</span> with an <span class="lnk">unassigned link</span>.</b> A second row of text with a <span class="lnk">web link</span>.</p>
  </div>
  <div class="result" style="top:184px">
    <p class="snip" style="left:20px"><b>A paragraph of <span class="red">text</span> with an <span class="lnk">unassigned link</span>.</b> A second row of text with a <span class="lnk">web link</span>.</p>
    <div class="photo" role="img" aria-label="Photo of a modern villa at dusk above a pool" style="right:0;background:linear-gradient(180deg,#7c93ad,#c8a27a 50%,#27485f)"></div>
  </div>
  <div class="result" style="top:268px">
    <div class="photo" role="img" aria-label="Photo of a villa with wooden deck and pool" style="left:0;background:linear-gradient(180deg,#5f86b3,#d9d7d2 50%,#8c6a4f)"></div>
    <p class="snip" style="left:140px"><b>A paragraph of <span class="red">text</span> with an <span class="lnk">unassigned link</span>.</b> A second row of text with a <span class="lnk">web link</span>.</p>
  </div>
  <div class="result" style="top:352px">
    <p class="snip" style="left:20px"><b>A paragraph of <span class="red">text</span> with an <span class="lnk">unassigned link</span>.</b> A second row of text with a <span class="lnk">web link</span>.</p>
    <div class="photo" role="img" aria-label="Photo of a tropical resort house with thatched roof and pool" style="right:0;background:linear-gradient(180deg,#3f86d8,#8e6a4a 50%,#2fa6a0)"></div>
  </div>
  <div class="pager" style="left:16px">&#8249; Previous Page</div>
  <div class="pager" style="right:16px">Next Page &#8250;</div>
</section>

<!-- Property detail -->
<section class="screen" style="left:654px;top:630px">
  <svg class="nav-home"><use href="#ico-home"/></svg>
  <svg class="nav-right" style="width:20px;height:20px"><use href="#ico-menu"/></svg>
  <div class="detail-photo" role="img" aria-label="Photo of a lit modern villa at dusk with infinity pool"></div>
  <h2 class="detail-title">Villa Brightkey</h2>
  <p class="body-copy" style="top:236px;left:45px;right:45px">Rustic historical farmhouse on top of a hill outside of Sineu within a protected area full of mediterranean oak trees, pine trees etc.</p>
  <p class="body-copy" style="top:290px;left:45px;right:45px">3 bedrooms | bathroom | large equipped kitchen with granit and marble worktop and an antic bread oven | big living room with fireplace | pool | terraces | option to construc 2-3 bedrooms | all licences in older | natural stone house</p>
  <div class="request">Send Request Information</div>
</section>

</body>
</html>
```